HollowPine Ventures Inc. Business Card Design

My business is custom renovations and homes.I would need to have a new business logo created to go along with my company name. The business card should be of a modern style as this is the market I am focused on. I would need my contact information and website posted on the card. I would also like to list a few of the tasks I conduct on the card (such as: Renovations, Additions, Repairs, New Homes, Design, Consultations). On the reverse of the card I currently have just my logo and my motto, "Shaping A Bold Path". However, I am open to completely changing everything as I am starting a new year and would like to excel further. Any new ideas and suggestions are always welcomed. Thank you.

Target Market(s)

Upscale residential and commercial renovations and builds

Industry/Entity Type

Business

Contact Information for Business Card

I would like the design to be able to be laser cut or burnt onto a wooden business card. I will be creating one option of cards for really loyal customers (wooden) and a second option for the everyday customer (paper).

Font styles to use
Other font styles liked:
• Calibri / anything of mordern taste

Colors
f37122
5c5c5c
474747
ffffff

Requirements
Must have
• I would like the colours of my business to be a sharp orange and grey. I believe this will symbolize a modern style. I am open to other suggestions if this is not suitable for the designers tastes. My contact info as follows:
• Will Marsh
• President
• HollowPine Ventures Inc.
• 555-214-3987
• will@hollowpineventures.example
• I would like my website (currently under construction) hollowpineventures.example on the card aswell.
Nice to have
• Along with a modern logo representing HollowPine, I would like something on the card besides the logo and contact information. Perhaps a small background design. I feel it may be nice to have my services listed on the card (in smaller font on the bottom) Renovations, Additions, Repairs, Design, Consultations.
Should not have
• The business card should not have too many different colors. Should not have rounded corners.

```html
<!DOCTYPE html>
<html lang="en">
<head>
<meta charset="utf-8">
<title>HollowPine Ventures Inc. — Business Card</title>
<link rel="stylesheet" href="https://fonts.googleapis.com/css2?family=Ubuntu:ital,wght@0,400;0,500;1,400&family=Montserrat:wght@400;500;600&family=Michroma&display=swap">
<style>
  :root {
    --orange: #f37122;
    --grey: #5c5c5c;
    --grey-dark: #474747;
    --white: #ffffff;
    --card-dark: #2b2829;
    --stage: #e6eaec;
  }
  * { box-sizing: border-box; margin: 0; padding: 0; }
  html, body { width: 1200px; height: 960px; overflow: hidden; }
  body { background: var(--stage); position: relative; font-family: "Ubuntu", sans-serif; }

  .card {
    position: absolute;
    width: 560px;
    height: 320px;
    box-shadow: 0 14px 34px rgba(0,0,0,.22);
  }

  /* Front — dark */
  .card--front {
    left: 110px; top: 110px;
    background: linear-gradient(90deg, var(--card-dark) 0 38%, #3a3637 42%, #2e2b2c 50%, var(--card-dark) 100%);
    color: var(--white);
  }
  .front__block {
    position: absolute; left: 56px; top: 62px;
    width: 120px; height: 120px;
    background: #4b4748;
  }
  .front__brand {
    position: absolute; left: 270px; top: 78px; width: 260px; text-align: center;
  }
  .brand__name {
    font-family: "Ubuntu", sans-serif; font-weight: 500;
    font-size: 48px; line-height: 1; letter-spacing: -0.5px;
  }
  .brand__sub {
    font-family: "Ubuntu", sans-serif; font-weight: 400;
    font-size: 16px; letter-spacing: 6px; color: var(--orange); margin-top: 8px;
  }
  .brand__tagline {
    font-family: "Ubuntu", sans-serif; font-style: italic;
    font-size: 20px; color: var(--orange); margin-top: 12px;
  }
  .front__services {
    position: absolute; left: 0; right: 28px; bottom: 30px;
    text-align: right; font-size: 17px; color: var(--white);
  }
  .front__services .sep { color: var(--orange); margin: 0 8px; }

  /* Back — white */
  .card--back {
    left: 530px; top: 500px;
    background: var(--white);
    border-bottom: 4px solid var(--grey-dark);
  }
  .back__head {
    position: absolute; left: 30px; top: 28px;
    padding-left: 14px; border-left: 5px solid var(--orange);
  }
  .back__name {
    font-family: "Michroma", sans-serif; font-size: 24px; color: var(--grey-dark); line-height: 1.1;
  }
  .back__role {
    font-family: "Montserrat", sans-serif; font-weight: 600; font-size: 12px;
    letter-spacing: 1px; color: var(--orange);
  }
  .back__contacts {
    position: absolute; left: 30px; top: 106px; list-style: none;
    font-family: "Montserrat", sans-serif; font-size: 13.5px; color: var(--grey-dark);
  }
  .back__contacts li { display: flex; align-items: center; gap: 12px; margin-bottom: 9px; }
  .back__contacts svg { width: 16px; height: 16px; flex: none; }
  .back__block {
    position: absolute; right: 44px; top: 56px;
    width: 96px; height: 96px; background: #e2e2e2;
  }
  .back__brand {
    position: absolute; right: 30px; bottom: 34px; text-align: right;
  }
  .back__brand .brand__name { color: var(--grey-dark); font-size: 34px; }
  .back__brand .brand__sub { font-size: 11px; letter-spacing: 5px; margin-top: 4px; }
</style>
</head>
<body>

<section class="card card--front" aria-label="Business card front">
  <div class="front__block" aria-hidden="true"></div>
  <div class="front__brand">
    <div class="brand__name">HollowPine</div>
    <div class="brand__sub">VENTURES INC.</div>
    <div class="brand__tagline">Shaping A Bold Path</div>
  </div>
  <p class="front__services">
    Renovations<span class="sep">|</span>Additions<span class="sep">|</span>Repairs<span class="sep">|</span>Design<span class="sep">|</span>Consultations
  </p>
</section>

<section class="card card--back" aria-label="Business card back">
  <div class="back__head">
    <div class="back__name">Will Marsh</div>
    <div class="back__role">President</div>
  </div>
  <ul class="back__contacts">
    <li>
      <svg viewBox="0 0 16 16" aria-hidden="true"><path fill="#f37122" d="M2 6c0-2 2.5-3 6-3s6 1 6 3v1h-3V5.5H5V7H2zM4 8h8l1.5 5h-11z"/></svg>
      555-214-3987
    </li>
    <li>
      <svg viewBox="0 0 16 16" aria-hidden="true"><rect x="1" y="3" width="14" height="10" fill="#f37122"/><path d="M1.5 3.5 8 9l6.5-5.5" fill="none" stroke="#fff" stroke-width="1.2"/></svg>
      will@hollowpineventures.example
    </li>
    <li>
      <svg viewBox="0 0 16 16" aria-hidden="true"><g fill="none" stroke="#f37122" stroke-width="1.3"><circle cx="8" cy="8" r="6.5"/><ellipse cx="8" cy="8" rx="2.8" ry="6.5"/><path d="M1.5 8h13M2.5 5h11M2.5 11h11"/></g></svg>
      hollowpineventures.example
    </li>
  </ul>
  <div class="back__block" aria-hidden="true"></div>
  <div class="back__brand">
    <div class="brand__name">HollowPine</div>
    <div class="brand__sub">VENTURES INC.</div>
  </div>
</section>

</body>
</html>
```